Quelmira Business Card

Need a business card for our business.

Attached are our Logos. There is either the white and black all the all red with white. Either Logo can be used.

The winner will be provided the details for phone number and address.

Good Luck!

Business

```html
<!DOCTYPE html>
<html lang="en">
<head>
<meta charset="utf-8">
<title>Quelmira Industries – Business Card</title>
<link rel="stylesheet" href="https://fonts.googleapis.com/css2?family=Josefin+Sans:wght@400;600;700&display=swap">
<style>
  :root {
    --backdrop: #2b1715;
    --kraft: #b8915e;
    --kraft-edge: #a47f4f;
    --ink: #2a1d12;
    --brand-red: #701816;
  }
  * { box-sizing: border-box; margin: 0; padding: 0; }
  html, body {
    width: 1200px; height: 716px; overflow: hidden;
    background: var(--backdrop);
    font-family: "Josefin Sans", sans-serif;
    color: var(--ink);
  }
  .canvas { position: relative; width: 1200px; height: 716px; }

  .card {
    position: absolute;
    width: 520px; height: 298px;
    background: var(--kraft);
    border-radius: 4px;
    box-shadow: 0 10px 30px rgba(0,0,0,.45);
  }
  .card--front { left: 50px; top: 209px; }
  .card--back  { left: 630px; top: 209px; }

  /* Front */
  .front-mark {
    position: absolute; left: 0; right: 0; top: 86px;
    text-align: center; color: var(--brand-red); font-weight: 700;
  }
  .front-mark__name { font-size: 64px; line-height: 1; letter-spacing: 1px; }
  .front-mark__sub  { font-size: 26px; letter-spacing: 20px; margin-top: 14px; padding-left: 20px; }

  /* Back */
  .frame {
    position: absolute; inset: 14px;
    border: 1.5px solid var(--ink);
  }
  .rule { position: absolute; left: 0; right: 0; border-top: 1.5px solid var(--ink); }
  .rule--1 { top: 52px; }
  .rule--2 { top: 86px; }
  .rule--3 { top: 124px; }
  .rule--v { position: absolute; left: 250px; top: 94px; height: 22px; border-left: 1.5px solid var(--ink); }

  .holder-name {
    position: absolute; right: 18px; top: 14px;
    font-size: 26px; font-weight: 600; letter-spacing: 13px;
    color: var(--brand-red);
  }
  .holder-role {
    position: absolute; right: 70px; top: 63px;
    font-size: 12px; font-weight: 600; letter-spacing: 5px;
    color: var(--brand-red);
  }
  .contact-email { position: absolute; left: 14px; top: 100px; font-size: 10px; letter-spacing: .5px; }
  .contact-mobile { position: absolute; left: 268px; top: 100px; font-size: 10px; letter-spacing: 1.5px; }

  .back-mark {
    position: absolute; left: 18px; top: 150px;
    color: var(--brand-red); font-weight: 700;
  }
  .back-mark__name { font-size: 34px; line-height: 1; }
  .back-mark__sub  { font-size: 13px; letter-spacing: 10px; margin-top: 6px; }

  .address {
    position: absolute; left: 268px; top: 148px;
    font-size: 10px; line-height: 1.6; letter-spacing: 1.2px;
  }
  .address p + p { margin-top: 6px; }
  .address .web { font-weight: 600; }
</style>
</head>
<body>
<main class="canvas">
  <section class="card card--front" aria-label="Card front">
    <div class="front-mark">
      <div class="front-mark__name">QUELMIRA</div>
      <div class="front-mark__sub">INDUSTRIES</div>
    </div>
  </section>

  <section class="card card--back" aria-label="Card back">
    <div class="frame">
      <div class="holder-name">DORIAN VALE</div>
      <div class="rule rule--1"></div>
      <div class="holder-role">MANAGING DIRECTOR</div>
      <div class="rule rule--2"></div>
      <div class="contact-email">dorian@quelmiraindustries.com</div>
      <div class="rule--v"></div>
      <div class="contact-mobile">MOBILE: XXX XXX XXXX</div>
      <div class="rule rule--3"></div>

      <div class="back-mark">
        <div class="back-mark__name">QUELMIRA</div>
        <div class="back-mark__sub">INDUSTRIES</div>
      </div>

      <div class="address">
        <p>Your Address, Building,<br>City XXXXX Country</p>
        <p>TEL: XXX XXX XXXX</p>
        <p>FAX: XXX XXX XXXX</p>
        <p class="web">www.quelmiraindustries.com</p>
      </div>
    </div>
  </section>
</main>
</body>
</html>
```